looking for sleek business card to standout from the crowd!

We are a young biotechnology company looking to help you personalize your health through understanding your genetic make up. We need you help in making a clean but sleek business card design using our new logo. The goal? Any time we give our cards out, people say "nice card!" The feel we are going for is "modern-techy". We don't want to come across as an old, giant pharma company, but not trying to be a hipster either.

Target Market(s)

healthcare and biotechnology industry.

Industry/Entity Type

Biotechnology

Contact Information for Business Card

Info to include on the card will be NAME, TITLE, EMAIL, PHONE. The companies website (www.corvalinbio.com) should also be on the card some where. Would like the logo, when printed, to be raised.

Requirements
Must have
• The logo we have attached in the color it is in. Fonts for text should lean toward more professional/tech.
Nice to have
• Prefer white/light color background
Should not have
• cartoons, landscape backgrounds images.

```html
<!DOCTYPE html>
<html lang="en">
<head>
<meta charset="utf-8">
<title>Corvalin business card</title>
<link rel="stylesheet" href="https://fonts.googleapis.com/css2?family=Montserrat:wght@400;600;700&display=swap">
<style>
  :root {
    --page-bg: #e9ebee;
    --card-dark: #1c1d1f;
    --card-light: #ffffff;
    --brand-blue: #1a72bd;
    --accent-green: #86c441;
    --text-grey: #6d6f72;
    --shadow: rgba(0, 0, 0, 0.18);
  }
  * { box-sizing: border-box; margin: 0; padding: 0; }
  html, body {
    width: 1200px;
    height: 864px;
    overflow: hidden;
    background: var(--page-bg);
    font-family: "Montserrat", sans-serif;
  }
  .sheet {
    width: 1200px;
    height: 864px;
    display: flex;
    align-items: center;
    justify-content: center;
    gap: 40px;
  }
  .card {
    width: 540px;
    height: 309px;
    border-radius: 4px;
    box-shadow: 0 10px 28px var(--shadow);
    position: relative;
  }
  .card--front {
    background: linear-gradient(160deg, #26282b 0%, var(--card-dark) 60%, #141516 100%);
    display: flex;
    align-items: center;
    justify-content: center;
  }
  .card--back { background: var(--card-light); }
  .wordmark {
    font-weight: 700;
    font-size: 50px;
    letter-spacing: 2px;
    color: var(--brand-blue);
    line-height: 1;
  }
  .card--back .wordmark {
    position: absolute;
    top: 76px;
    left: 0;
    right: 0;
    text-align: center;
    font-size: 40px;
  }
  .details {
    position: absolute;
    top: 196px;
    left: 0;
    right: 0;
    display: flex;
    justify-content: center;
    align-items: center;
    gap: 18px;
  }
  .person { text-align: right; }
  .person__name {
    font-weight: 600;
    font-size: 19px;
    color: var(--brand-blue);
  }
  .person__title {
    font-size: 13px;
    color: var(--text-grey);
    margin-top: 2px;
  }
  .divider {
    width: 2px;
    height: 54px;
    background: var(--brand-blue);
  }
  .contact { list-style: none; }
  .contact__item {
    display: flex;
    align-items: center;
    gap: 8px;
    font-size: 13px;
    color: var(--text-grey);
    line-height: 19px;
  }
  .contact__icon { width: 12px; height: 12px; flex: none; }
</style>
</head>
<body>
<main class="sheet">
  <section class="card card--front" aria-label="Card front">
    <p class="wordmark">CORVALIN</p>
  </section>

  <section class="card card--back" aria-label="Card back">
    <p class="wordmark">CORVALIN</p>
    <div class="details">
      <div class="person">
        <p class="person__name">Daniel Hartwell</p>
        <p class="person__title">President</p>
      </div>
      <div class="divider"></div>
      <ul class="contact">
        <li class="contact__item">
          <svg class="contact__icon" viewBox="0 0 12 12" aria-hidden="true"><path d="M2.5 1 L4.5 3.2 L3.5 4.6 Q4.6 7 7.4 8.5 L8.8 7.5 L11 9.5 L9.6 11 Q4.8 10.6 1 3 Z" fill="#86c441"/></svg>
          014-555-0192
        </li>
        <li class="contact__item">
          <svg class="contact__icon" viewBox="0 0 12 12" aria-hidden="true"><rect x="0.5" y="2.5" width="11" height="7.5" fill="#86c441"/><path d="M0.5 2.5 L6 6.8 L11.5 2.5" fill="none" stroke="#fff" stroke-width="1"/></svg>
          info@corvalinbio.com
        </li>
        <li class="contact__item">
          <svg class="contact__icon" viewBox="0 0 12 12" aria-hidden="true"><g fill="none" stroke="#86c441" stroke-width="1.1"><circle cx="6" cy="6" r="5"/><ellipse cx="6" cy="6" rx="2.2" ry="5"/><path d="M1 6 H11 M2 3.3 H10 M2 8.7 H10"/></g></svg>
          corvalinbio.com
        </li>
      </ul>
    </div>
  </section>
</main>
</body>
</html>
```